Website redesign

Looking to redesign our existing website. (quill7meadows.com.au)
New design needs to be bright, fun and have an easy flowing.
The website needs to be design with call to action.

Some examples of other websites:
fernquaylo.com
tovanmilk.com.au

We are happy with the content of our existing website.

Target Market(s)

other businesses

Industry/Entity Type

Business Service

Number of Pages Required

5+ page

Requirements
Must have
• Theme redesign
Cool animation similar to fernquaylo.com

```html
<!DOCTYPE html>
<html lang="en">
<head>
<meta charset="utf-8">
<title>Quill7 Meadows — Virtual Assistants</title>
<link rel="stylesheet" href="https://fonts.googleapis.com/css2?family=Montserrat:wght@300;400;500;600;700;800&display=swap">
<style>
:root{
  --blue:#1ba8e0;
  --blue-soft:#cbe9f6;
  --navy:#0e1a2b;
  --navy-2:#13263c;
  --ink:#16202c;
  --grey:#5b6470;
  --muted:#c4c9cf;
  --panel:#f1f3f5;
  --white:#ffffff;
}
*{margin:0;padding:0;box-sizing:border-box}
html,body{width:1200px;height:3876px;overflow:hidden;background:var(--white)}
body{position:relative;font-family:'Montserrat',sans-serif;color:var(--ink)}
.abs{position:absolute}
.accent{color:var(--blue)}

/* header */
.brand{position:absolute;left:95px;top:28px;display:flex;align-items:center;gap:8px;font-weight:700;font-size:28px;color:var(--navy)}
.brand-dot{width:12px;height:12px;border-radius:50%;background:var(--blue)}
.nav{position:absolute;right:93px;top:34px;display:flex;gap:23px;font-size:13px;font-weight:500;color:var(--ink)}

/* hero */
.hero-text{z-index:2}
.hero-title{left:95px;top:224px;font-size:41px;font-weight:800;color:var(--blue);letter-spacing:1px;white-space:nowrap}
.hero-sub{left:95px;top:276px;font-size:26px;font-weight:400;letter-spacing:3.6px;color:var(--ink);white-space:nowrap}
.hero-rule{left:95px;top:336px;width:137px;height:5px;background:var(--navy)}
.hero-lead{left:95px;top:372px;font-size:21px;line-height:32px;letter-spacing:2px;font-weight:400;white-space:nowrap}
.btn-call{left:98px;top:462px;width:146px;height:32px;background:var(--blue);color:#fff;font-size:14px;font-weight:700;display:flex;align-items:center;justify-content:center;gap:6px;box-shadow:0 6px 14px rgba(27,168,224,.35);border-radius:2px}
.btn-quote{left:274px;top:462px;width:146px;height:32px;border:1.5px solid var(--blue);color:var(--blue);font-size:14px;font-weight:600;display:flex;align-items:center;justify-content:center;border-radius:2px}
.hero-art{left:650px;top:128px;width:508px;height:443px;border-radius:12px;z-index:1;background:linear-gradient(160deg,#f4f6f8 0%,#e9f6fc 55%,#bfe6f6 100%)}

/* intro */
.intro-title{left:0;top:746px;width:1200px;text-align:center;font-size:33px;font-weight:800;line-height:41px;letter-spacing:.8px}
.intro-copy{left:270px;top:848px;width:660px;text-align:center;font-size:14px;line-height:22.5px;color:var(--grey)}
.video{left:220px;top:955px;width:762px;height:388px;background:linear-gradient(120deg,#2f6fb8 0%,#4b6f93 45%,#2a3240 100%);box-shadow:0 16px 24px rgba(0,0,0,.2)}

/* section headings */
.sec-title{left:0;width:1200px;text-align:center;font-size:32px;font-weight:800;letter-spacing:1px}
.sec-rule{left:532px;width:137px;height:5px;background:var(--navy)}

/* process */
.step-art{left:128px;top:1609px;width:398px;height:263px;border-radius:40% 30% 20% 30%;background:linear-gradient(135deg,#eef2f8 0%,#d6e4f4 60%,#3a3fa0 100%)}
.timeline-line{left:600px;top:1600px;width:2px;height:281px;background:var(--muted)}
.tl-dot{width:14px;height:14px;border-radius:50%;background:#b9bec4;left:594px}
.tl-dot.active{width:28px;height:28px;left:587px;background:#fff;border:2px solid #d6eaf5;display:flex;align-items:center;justify-content:center}
.tl-dot.active::after{content:"";width:18px;height:18px;border-radius:50%;background:var(--blue)}
.step-num{left:681px;top:1622px;font-size:45px;font-weight:800;color:#e3e5e8;letter-spacing:1px}
.step-head{left:681px;top:1692px;font-size:16px;font-weight:600;color:var(--blue)}
.step-copy{left:681px;top:1722px;width:400px;font-size:14px;line-height:22.5px;color:var(--grey)}

/* services */
.services-intro{left:200px;top:2112px;width:800px;text-align:center;font-size:14px;line-height:23px;color:var(--grey)}
.services-intro b{color:var(--ink);font-weight:600}
.svc{display:flex;gap:17px;font-size:14px;font-weight:600;line-height:20px;width:340px}
.svc svg{flex:none;margin-top:2px}
.cta-line{left:0;top:2420px;width:1200px;text-align:center;font-size:34px;font-weight:800;line-height:38px}

/* dark band */
.band{left:0;top:2623px;width:1200px;height:582px;background:linear-gradient(180deg,var(--navy) 0%,var(--navy-2) 100%)}
.band-title{left:0;top:2696px;width:1200px;text-align:center;font-size:32px;font-weight:800;color:#fff;letter-spacing:.5px}
.band-sub{left:0;top:2755px;width:1200px;text-align:center;font-size:14px;color:#fff;font-weight:500}
.feature{width:260px;text-align:center;color:#fff;font-size:15px;font-weight:600;line-height:20px}
.feature svg{display:block;margin:0 auto 14px}

/* quote */
.agent-photo{left:647px;top:3136px;width:316px;height:489px;border-radius:150px 150px 0 0;background:linear-gradient(180deg,#c59a6e 0%,#ecdccb 35%,#f6f4f1 100%)}
.quote-title{left:209px;top:3272px;font-size:33px;font-weight:800;letter-spacing:.5px}
.quote-sub{left:209px;top:3328px;font-size:14px;line-height:18px;color:var(--grey)}
.form-panel{left:209px;top:3387px;width:741px;height:238px;background:linear-gradient(90deg,#eef0f2 0%,#f3f4f6 70%,rgba(243,244,246,0) 100%)}
.field{border-bottom:1px solid #b8bdc3;font-size:10px;color:#7a828c;padding-bottom:9px}
.submit{left:209px;top:3650px;width:147px;height:34px;background:var(--blue);color:#fff;font-size:14px;font-weight:700;letter-spacing:.5px;display:flex;align-items:center;justify-content:center;box-shadow:0 6px 14px rgba(27,168,224,.35)}
.newsletter{left:387px;top:3661px;font-size:10px;color:#8a9199;display:flex;align-items:center;gap:8px}
.newsletter span.box{width:12px;height:12px;border:1px solid var(--blue)}

/* footer */
.footer{left:0;top:3755px;width:1200px;height:121px;background:var(--navy)}
.footer .brand{color:#fff;top:44px}
.copyright{right:93px;top:55px;font-size:10px;color:#fff;font-weight:500}
</style>
</head>
<body>

<header>
  <div class="brand"><span>Quill7</span><span class="brand-dot"></span></div>
  <nav class="nav"><span>Home</span><span>Our Story</span><span>Tips and Tricks</span><span>Contact Us</span><span>FAQs</span></nav>
</header>

<section class="hero">
  <div class="abs hero-art" role="img" aria-label="Illustration of a virtual assistant with headset on a monitor above a blue desk, with chat bubbles"></div>
  <h1 class="abs hero-text hero-title">VIRTUAL ASSISTANT?</h1>
  <p class="abs hero-text hero-sub">MORE LIKE VALUABLE ASSET!</p>
  <div class="abs hero-rule"></div>
  <p class="abs hero-text hero-lead">FULL-TIME VIRTUAL ASSISTANT<br>BETROTHED TO YOUR BUSINESS!</p>
  <a class="abs btn-call"><svg width="12" height="12" viewBox="0 0 24 24" fill="#fff"><path d="M6.6 10.8a15 15 0 0 0 6.6 6.6l2.2-2.2a1 1 0 0 1 1-.25 11.4 11.4 0 0 0 3.6.57 1 1 0 0 1 1 1V20a1 1 0 0 1-1 1A17 17 0 0 1 3 4a1 1 0 0 1 1-1h3.5a1 1 0 0 1 1 1c0 1.25.2 2.45.57 3.57a1 1 0 0 1-.25 1z"/></svg>07 5550 1842</a>
  <a class="abs btn-quote">Get a Quote</a>
</section>

<section class="intro">
  <h2 class="abs intro-title">OUTSOURCING. <span class="accent">A BIG WORD THAT MEANS<br>BIG THINGS FOR YOUR BUSINESS.</span></h2>
  <svg class="abs" style="left:993px;top:790px" width="57" height="45" viewBox="0 0 57 45" fill="none" stroke="#9aa2ab" stroke-width="2"><rect x="2" y="10" width="53" height="33" rx="5"/><path d="M20 10V4h17v6M2 24h53"/><rect x="25" y="20" width="7" height="7"/></svg>
  <p class="abs intro-copy">Virtual Assistants are the superheroes of the modern office. They can do everything your team can do on a computer at a fraction of the price! (Well, maybe not high five you when you've had a win, but a virtual high five is definitely on the table!)</p>
  <svg class="abs" style="left:95px;top:1221px" width="54" height="50" viewBox="0 0 54 50" fill="none" stroke="#9aa2ab" stroke-width="2.5"><path d="M8 3h38a5 5 0 0 1 5 5v22a5 5 0 0 1-5 5h-6l8 12-18-12H8a5 5 0 0 1-5-5V8a5 5 0 0 1 5-5z"/><circle cx="17" cy="19" r="1.5" fill="#9aa2ab"/><circle cx="27" cy="19" r="1.5" fill="#9aa2ab"/><circle cx="37" cy="19" r="1.5" fill="#9aa2ab"/></svg>
  <div class="abs video" role="img" aria-label="Video still of two team members standing in front of a blue brick wall"></div>
  <svg class="abs" style="left:563px;top:1110px" width="76" height="76" viewBox="0 0 76 76" fill="none" stroke="#fff" stroke-width="3"><circle cx="38" cy="38" r="35"/><path d="M30 24l22 14-22 14z" stroke-linejoin="round"/></svg>
</section>

<section class="process">
  <h2 class="abs sec-title" style="top:1478px">THE <span class="accent">PROCESS</span></h2>
  <div class="abs sec-rule" style="top:1534px"></div>
  <div class="abs step-art" role="img" aria-label="Illustration of glasses resting on books with a graduation cap and a certificate"></div>
  <div class="abs timeline-line"></div>
  <div class="abs tl-dot active" style="top:1586px"></div>
  <div class="abs tl-dot" style="top:1664px"></div>
  <div class="abs tl-dot" style="top:1735px"></div>
  <div class="abs tl-dot" style="top:1805px"></div>
  <div class="abs tl-dot" style="top:1874px"></div>
  <div class="abs step-num">STEP 01</div>
  <h3 class="abs step-head">Provide Your Preferred Qualifications.</h3>
  <p class="abs step-copy">Set up a call with our team to specify the requirements and qualifications you're searching for in a Virtual Assistant. This will be our checklist for your perfect assistant! From there, we'll take care of shortlisting, testing, background checking and recruiting.</p>
  <svg class="abs" style="left:1020px;top:1929px" width="64" height="34" viewBox="0 0 64 34" fill="none" stroke="#8a929b" stroke-width="2" stroke-linejoin="round"><path d="M2 3h6l12 14L8 31H2l12-14z"/><path d="M22 3h6l12 14-12 14h-6l12-14z"/><path d="M42 3h6l12 14-12 14h-6l12-14z"/></svg>
</section>

<section class="services">
  <h2 class="abs sec-title" style="top:2028px">OUR <span class="accent">SERVICES</span></h2>
  <div class="abs sec-rule" style="top:2082px"></div>
  <p class="abs services-intro">We'll help you save tens (or even hundreds!) of thousands of dollars per year. But what do WE actually do?<br><b>GLAD YOU ASKED!</b></p>
  <svg class="abs" style="left:0;top:2293px" width="66" height="79" viewBox="0 0 66 79" fill="none" stroke="#9aa2ab" stroke-width="3"><path d="M8 66A32 32 0 1 1 20 72L4 77z"/><path d="M24 48l18-20"/><circle cx="25" cy="30" r="3"/><circle cx="41" cy="46" r="3"/></svg>
  <div class="abs svc" style="left:211px;top:2219px"><svg width="22" height="18" viewBox="0 0 22 18"><path d="M2 9l6 6L20 2" fill="none" stroke="#1ba8e0" stroke-width="3.5"/></svg><span>We recruit <span class="accent">Virtual Assistants</span> (a.k.a office<br>legends!), and</span></div>
  <div class="abs svc" style="left:651px;top:2219px"><svg width="22" height="18" viewBox="0 0 22 18"><path d="M2 9l6 6L20 2" fill="none" stroke="#1ba8e0" stroke-width="3.5"/></svg><span>Provide the <span class="accent">tech support</span> for these<br>superheroes!</span></div>
  <div class="abs svc" style="left:211px;top:2303px"><svg width="22" height="18" viewBox="0 0 22 18"><path d="M2 9l6 6L20 2" fill="none" stroke="#1ba8e0" stroke-width="3.5"/></svg><span>Set up the <span class="accent">phone system</span><br>(their own Bat Phone!)</span></div>
  <div class="abs svc" style="left:651px;top:2303px"><svg width="22" height="18" viewBox="0 0 22 18"><path d="M2 9l6 6L20 2" fill="none" stroke="#1ba8e0" stroke-width="3.5"/></svg><span>We manage Virtual Assistants and keep<br>them in <span class="accent">tip-top shape!</span></span></div>
  <p class="abs cta-line"><span class="accent">See?</span> It's that simple! <span class="accent">The only thing to do now is<br>to finally get started on the quote...</span><br>just scroll down a little more.</p>
</section>

<section class="why">
  <div class="abs band"></div>
  <h2 class="abs band-title">IT'S <span class="accent">QUILL7 MEADOWS TIME</span></h2>
  <p class="abs band-sub">Why are we your new best outsourcing friend?</p>

  <div class="abs feature" style="left:147px;top:2832px">
    <svg width="56" height="54" viewBox="0 0 56 54" fill="none" stroke="#1ba8e0" stroke-width="2.5"><rect x="6" y="12" width="44" height="32" rx="2"/><path d="M2 48h52"/><circle cx="28" cy="24" r="5" stroke="#fff"/><path d="M19 40c2-6 16-6 18 0" stroke="#fff"/><rect x="20" y="4" width="16" height="8"/></svg>
    Your Own Virtual<br>Assistant</div>
  <div class="abs feature" style="left:470px;top:2832px">
    <svg width="50" height="56" viewBox="0 0 50 56" fill="none" stroke="#1ba8e0" stroke-width="2.5"><rect x="4" y="2" width="32" height="50" rx="2"/><circle cx="32" cy="16" r="9" stroke="#fff"/><path d="M32 11v10" stroke="#fff"/><path d="M10 30h20M10 37h20M10 44h12"/><rect x="36" y="30" width="10" height="22" rx="2" stroke="#fff"/></svg>
    One Invoice Per Month</div>
  <div class="abs feature" style="left:793px;top:2832px">
    <svg width="46" height="56" viewBox="0 0 46 56" fill="none" stroke="#1ba8e0" stroke-width="2.5"><path d="M16 12l-6-9h26l-6 9"/><path d="M16 12h14c9 6 14 16 14 26 0 10-8 15-21 15S2 48 2 38c0-10 5-20 14-26z"/><circle cx="23" cy="34" r="9" stroke="#fff"/><path d="M19 38l8-8" stroke="#fff"/></svg>
    No Super or TAX</div>

  <div class="abs feature" style="left:147px;top:3002px">
    <svg width="58" height="50" viewBox="0 0 58 50" fill="none" stroke="#fff" stroke-width="2.5"><rect x="3" y="10" width="52" height="36" rx="4"/><path d="M20 10V3h18v7"/><path d="M3 24h52" stroke="#1ba8e0"/><rect x="25" y="20" width="8" height="8" stroke="#1ba8e0"/></svg>
    Dedicated To Your<br>Business Only</div>
  <div class="abs feature" style="left:470px;top:3002px">
    <svg width="34" height="56" viewBox="0 0 34 56" fill="none" stroke="#1ba8e0" stroke-width="2.5"><rect x="3" y="2" width="28" height="52" rx="4"/><path d="M12 7h10M14 48h6"/><path d="M15 26l4-4M14 30l6-6" stroke="#fff"/></svg>
    Dedicated Phone System</div>
  <div class="abs feature" style="left:793px;top:3002px">
    <svg width="58" height="54" viewBox="0 0 58 54" fill="none" stroke="#1ba8e0" stroke-width="2.5"><rect x="3" y="3" width="48" height="36" rx="2"/><circle cx="27" cy="20" r="7" stroke="#fff"/><circle cx="27" cy="20" r="2.5" stroke="#fff"/><path d="M38 39v12l8-7h9V32"/><path d="M10 46h18"/></svg>
    IT Setup and Support</div>
</section>

<section class="quote">
  <h2 class="abs quote-title">GET A <span class="accent">QUOTE</span></h2>
  <p class="abs quote-sub">Fill in the form below to get a Quote<br>for your own personal Virtual Assistant</p>
  <div class="abs form-panel"></div>
  <div class="abs field" style="left:244px;top:3412px;width:406px">Business Name</div>
  <div class="abs field" style="left:244px;top:3456px;width:186px">First Name</div>
  <div class="abs field" style="left:462px;top:3456px;width:188px">Last Name</div>
  <div class="abs field" style="left:244px;top:3500px;width:186px">Contact Number</div>
  <div class="abs field" style="left:462px;top:3500px;width:188px">Email ID</div>
  <div class="abs field" style="left:244px;top:3545px;width:406px;padding-bottom:40px">Describe the tasks you'll need from your Virtual Assistant</div>
  <div class="abs agent-photo" role="img" aria-label="Photo of a smiling support agent wearing a headset and holding a tablet"></div>
  <svg class="abs" style="left:1010px;top:3440px" width="92" height="94" viewBox="0 0 92 94" fill="none" stroke="#9aa2ab" stroke-width="2" stroke-linejoin="round"><path d="M40 6l38-4-12 20z"/><path d="M40 6l14 8 12 8M54 14l-4 10"/><path d="M4 72l40-16-4 30z"/><path d="M4 72l22 4 18-20M26 76l14 10"/><path d="M52 66l14-8M56 74l12-6"/></svg>
  <a class="abs submit">SUBMIT</a>
  <label class="abs newsletter"><span class="box"></span>Subscribe to our newsletter</label>
</section>

<footer class="abs footer">
  <div class="brand"><span>Quill7</span><span class="brand-dot"></span></div>
  <p class="abs copyright">© 2020 QUILL7 MEADOWS | ALL RIGHTS RESERVED.</p>
</footer>

</body>
</html>
```